Harrowden Metal recycling, a business card/logo for our industrial family metal recycling company

A new business card design/logo for our long established family metal recycling company.
I have a logo for our property company which was designed a few months ago on pixel forge which I would like to be very close to this design but have a more industrial feel to it and in a darker blue colour, please see attachments.

Target Market(s)

industries that produce metal waste for recycling, construction sites, engineering companies, manufactures, builders, plumbers, electricians, general house holders.

Industry/Entity Type

Recycling

Contact Information for Business Card

owner/director...Martin harrowden
e-mail....info@harrowdenscrapworks.co.uk
web address.....harrowdenscrapworks.co.uk

Font styles to use
Serif
Sans Serif

Colors
0255a3
ffffff

Requirements
Must have
• -dark blue business card on front.
-white on the back, see contact details, e-mail address for metal company.
-to have an industrial feel to it.
-harrowden logo as business card attached but (harrowden metal recycling)
please remove the little roof/arrow above harrowden as this was relevant to property company.
Nice to have
• please see our website harrowdenscrapworks.co.uk with all details
being correct however I would like to refresh the logo to more like the harrowden property investment business card logo attached.
Should not have
• should not contain details from property investments card as this design is for the metal recycling company.

```html
<!DOCTYPE html>
<html lang="en">
<head>
<meta charset="utf-8">
<title>Harrowden Metal Recycling – Business Card</title>
<link href="https://fonts.googleapis.com/css2?family=Open+Sans:wght@300;400;600;700&display=swap" rel="stylesheet">
<style>
  :root {
    --brand-blue: #0255a3;
    --deep-blue: #0a4a94;
    --white: #ffffff;
    --ink: #222222;
    --charcoal: #232323;
    --backdrop: #b6b9ba;
  }
  * { margin: 0; padding: 0; box-sizing: border-box; }
  html, body { width: 1026px; height: 1200px; overflow: hidden; }
  body {
    background: var(--backdrop);
    font-family: "Open Sans", Arial, sans-serif;
    position: relative;
  }
  .card {
    position: absolute;
    left: 31px;
    width: 965px;
    height: 550px;
    overflow: hidden;
  }
  /* Front */
  .card-front { top: 38px; background: var(--brand-blue); color: var(--white); }
  .front-photo {
    position: absolute; inset: 0;
    background:
      radial-gradient(ellipse at 40% 85%, rgba(0,40,100,0.55), transparent 60%),
      linear-gradient(180deg, #2d6fc0 0%, #1a5db0 45%, #0c4c9a 100%);
  }
  .front-name {
    position: absolute; left: 0; right: 0; top: 118px;
    text-align: center;
    font-weight: 300; font-size: 132px; line-height: 1;
    letter-spacing: 4px; text-transform: lowercase;
  }
  .front-tagline {
    position: absolute; left: 0; right: 0; top: 262px;
    text-align: center;
    font-size: 33px; font-weight: 400; letter-spacing: 22px;
    padding-left: 22px;
  }
  .front-since {
    position: absolute; left: 123px; right: 123px; top: 318px;
    display: flex; align-items: center; gap: 18px;
    font-size: 28px; font-weight: 600; letter-spacing: 2px;
  }
  .front-since .rule { flex: 1; height: 3px; background: var(--white); }
  .front-web {
    position: absolute; left: 0; right: 0; top: 462px;
    text-align: center; font-size: 34px; font-weight: 300;
  }
  /* Back */
  .card-back { top: 609px; background: var(--white); color: var(--ink); }
  .back-name {
    position: absolute; left: 0; right: 0; top: 30px;
    text-align: center; color: var(--brand-blue);
    font-weight: 300; font-size: 96px; line-height: 1;
    letter-spacing: 3px; text-transform: lowercase;
  }
  .back-tagline {
    position: absolute; left: 0; right: 0; top: 133px;
    text-align: center; color: var(--brand-blue);
    font-size: 24px; letter-spacing: 16px; padding-left: 16px;
  }
  .back-claim {
    position: absolute; left: 0; right: 0; top: 186px;
    text-align: center; font-size: 19px; font-weight: 700; color: var(--charcoal);
  }
  .person { position: absolute; left: 110px; top: 335px; }
  .person-name { font-size: 27px; line-height: 1.2; text-transform: uppercase; }
  .person-name .first { color: var(--brand-blue); font-weight: 700; }
  .person-name .last { color: var(--charcoal); font-weight: 400; }
  .person-role { font-size: 25px; color: var(--charcoal); font-weight: 400; }
  .divider {
    position: absolute; left: 410px; top: 250px;
    width: 3px; height: 240px; background: var(--brand-blue);
  }
  .contact-list { position: absolute; left: 445px; top: 253px; list-style: none; }
  .contact-item {
    display: flex; align-items: center;
    font-size: 23px; font-weight: 300; color: var(--charcoal);
    line-height: 1.35;
  }
  .contact-item .icon { width: 36px; height: 36px; margin-right: 35px; flex: none; fill: var(--brand-blue); }
  .contact-address { margin-bottom: 12px; }
  .contact-phone { margin-bottom: 14px; }
  .contact-web { margin-bottom: 14px; }
  .bottom-bar { position: absolute; left: 0; right: 0; bottom: 0; height: 25px; display: flex; }
  .bottom-bar .blue { width: 483px; background: var(--brand-blue); }
  .bottom-bar .dark { flex: 1; background: var(--charcoal); }
</style>
</head>
<body>
  <section class="card card-front">
    <div class="front-photo" role="img" aria-label="Photograph of an excavator grab over a scrap metal pile, tinted blue"></div>
    <div class="front-name">harrowden</div>
    <div class="front-tagline">METAL RECYCLING</div>
    <div class="front-since"><span class="rule"></span><span>SINCE 1950</span><span class="rule"></span></div>
    <div class="front-web">harrowdenscrapworks.co.uk</div>
  </section>

  <section class="card card-back">
    <div class="back-name">harrowden</div>
    <div class="back-tagline">METAL RECYCLING</div>
    <div class="back-claim">BUYERS OF ALL NON-FERROUS METALS AND CABLES IN CROYDON SINCE 1978</div>

    <div class="person">
      <div class="person-name"><span class="first">Martin</span><span class="last"> Harrowden</span></div>
      <div class="person-role">Director</div>
    </div>

    <div class="divider"></div>

    <ul class="contact-list">
      <li class="contact-item contact-address">
        <svg class="icon" viewBox="0 0 24 24" aria-hidden="true"><path d="M12 2a7 7 0 0 0-7 7c0 5.2 7 13 7 13s7-7.8 7-13a7 7 0 0 0-7-7zm0 9.5A2.5 2.5 0 1 1 12 6.5a2.5 2.5 0 0 1 0 5z"/></svg>
        <span>D.Harrowden Metals Ltd,<br>Unit 7, 42B Kelmore Road<br>London, SE19 4QT</span>
      </li>
      <li class="contact-item contact-phone">
        <svg class="icon" viewBox="0 0 24 24" aria-hidden="true"><path d="M6.6 10.8a15.1 15.1 0 0 0 6.6 6.6l2.2-2.2c.3-.3.7-.4 1-.2 1.1.4 2.3.6 3.6.6.6 0 1 .4 1 1V20c0 .6-.4 1-1 1A17 17 0 0 1 3 4c0-.6.4-1 1-1h3.5c.6 0 1 .4 1 1 0 1.3.2 2.5.6 3.6.1.3 0 .7-.2 1z"/></svg>
        <span>0208-555-0147</span>
      </li>
      <li class="contact-item contact-web">
        <svg class="icon" viewBox="0 0 24 24" aria-hidden="true"><path d="M12 2a10 10 0 1 0 0 20 10 10 0 0 0 0-20zm6.9 6h-2.9a15.6 15.6 0 0 0-1.4-3.6A8 8 0 0 1 18.9 8zM12 4c.8 1.2 1.5 2.5 1.9 4h-3.8c.4-1.5 1.1-2.8 1.9-4zM4.3 14a8 8 0 0 1 0-4h3.4a16 16 0 0 0 0 4zm.8 2h2.9c.3 1.3.8 2.5 1.4 3.6A8 8 0 0 1 5.1 16zM8 8H5.1a8 8 0 0 1 4.3-3.6C8.8 5.5 8.3 6.7 8 8zm4 12c-.8-1.2-1.5-2.5-1.9-4h3.8c-.4 1.5-1.1 2.8-1.9 4zm2.3-6H9.7a14.7 14.7 0 0 1 0-4h4.6a14.7 14.7 0 0 1 0 4zm.3 5.6c.6-1.1 1.1-2.3 1.4-3.6h2.9a8 8 0 0 1-4.3 3.6zm1.7-5.6a16 16 0 0 0 0-4h3.4a8 8 0 0 1 0 4z"/></svg>
        <span>harrowdenscrapworks.co.uk</span>
      </li>
      <li class="contact-item contact-email">
        <svg class="icon" viewBox="0 0 24 24" aria-hidden="true"><path d="M2 5h20v14H2zm2 2v.4l8 5.2 8-5.2V7zm0 2.8V17h16V9.8l-8 5.2z"/></svg>
        <span>info@harrowdenscrapworks.co.uk</span>
      </li>
    </ul>

    <div class="bottom-bar"><span class="blue"></span><span class="dark"></span></div>
  </section>
</body>
</html>
```